Business card design needed

Family General Practitioner/ Family Physician.
Logo is the logo of the Crestmoor Guild of Family Clinicians Australia
http://kvplm.tarevo.edu.au/PictureGallery/logos/pages/CGFC%20logo_jpg.htm

Reason: Just a bit more time to make changes and the weekend for me to look at things closely and to choose. Thanks, Lumi

Thanks for all the submissions. So many of them are really works of art. Not one of them are not good. The ones that I am eliminating are the ones that I think are not suitable for me personally only, and because if I don't, it makes it very difficult to decide as many of you are also sending me slight variations of a card. I have just decided to choose a second place card too. Can't thank you all enough. Good luck, Lumi. P.S - Working today till 10 pm as the card says :-), so probably won't be able to give a feedback till late Saturday night or Sunday morning here in Sydney, Australia. 

Reason: Just added a second place to the budget and realised that Australia is ahead of the rest of the world in the time zone (only :-) - don't want to offend anyone or start a debate!! ) , so Monday deadline will mean it will be a weekend for the rest of the world. Just wanted to give everyone more time to submit their best, especially since I will be picking a second card too. Can't thank everyone enough for the submissions. P.S - Not keen on photos on the card.

Contact Information for Business Card

Dr. Lumi Harcourt M.B.B.S., F.C.G.F.C
Family General Practitioner
Address, timings, phone and fax number on the back.

Requirements
Must have
• Timings
Mon 7 am - 7 pm
Tues 7 am - 12 pm
Wed 7 am - 10 pm
Thurs 7 am - 12 pm
Fri 7 am - 8 pm
Sat 8 am - 10 pm
Sun - Off

```html
<!DOCTYPE html>
<html lang="en">
<head>
<meta charset="utf-8">
<title>Dr. Lumi Harcourt – Business Card</title>
<link rel="stylesheet" href="https://fonts.googleapis.com/css2?family=Roboto+Condensed:wght@400;700&display=swap">
<style>
  :root {
    --brand-red: #e94057;
    --emblem-tint-light: #fbe3e7;
    --emblem-tint-deep: #f6c4cc;
    --paper: #ffffff;
    --ink: #2f2f33;
    --backdrop-centre: #ffffff;
    --backdrop-edge: #ececee;
    --card-shadow: rgba(0, 0, 0, 0.16);
  }
  * { margin: 0; padding: 0; box-sizing: border-box; }
  html, body { width: 1200px; height: 1000px; overflow: hidden; }
  body {
    position: relative;
    font-family: "Roboto Condensed", "Arial Narrow", sans-serif;
    background: radial-gradient(circle at 50% 50%, var(--backdrop-centre) 0%, var(--backdrop-centre) 25%, var(--backdrop-edge) 100%);
  }
  .card {
    position: absolute;
    top: 203px;
    width: 342px;
    height: 594px;
    box-shadow: 4px 5px 8px var(--card-shadow);
  }
  /* Front */
  .card-front {
    left: 150px;
    background: var(--brand-red);
    color: var(--paper);
    text-align: center;
  }
  .emblem-placeholder {
    position: absolute;
    left: 77px;
    top: 107px;
    width: 190px;
    height: 125px;
    background: linear-gradient(180deg, var(--emblem-tint-light) 0%, var(--emblem-tint-deep) 100%);
  }
  .doctor-name {
    position: absolute;
    left: 0; right: 0;
    top: 365px;
    font-size: 40px;
    font-weight: 700;
    letter-spacing: -0.3px;
  }
  .doctor-credentials {
    position: absolute;
    left: 0; right: 0;
    top: 413px;
    font-size: 17px;
    font-weight: 700;
    letter-spacing: 0.2px;
  }
  .doctor-role {
    position: absolute;
    left: 0; right: 0;
    top: 456px;
    font-size: 23.5px;
    font-weight: 700;
  }
  /* Back */
  .card-back {
    left: 708px;
    background: var(--paper);
  }
  .hours-panel {
    position: absolute;
    left: 0; top: 0;
    width: 100%;
    height: 395px;
    background: var(--brand-red);
    color: var(--paper);
    padding: 42px 0 0 23px;
  }
  .hours-title {
    font-size: 23px;
    font-weight: 700;
    margin-bottom: 13px;
  }
  .hours-table { border-collapse: collapse; }
  .hours-table td {
    font-size: 23px;
    font-weight: 400;
    height: 37.2px;
    padding: 0;
    vertical-align: middle;
  }
  .hours-table .day { width: 125px; }
  .contact-block {
    position: absolute;
    left: 23px;
    top: 436px;
    color: var(--ink);
    font-size: 17.5px;
    font-weight: 700;
    font-style: normal;
    line-height: 22px;
  }
  .contact-row { display: flex; }
  .contact-label {
    color: var(--brand-red);
    width: 19px;
    flex-shrink: 0;
  }
  .contact-gap { height: 23px; }
</style>
</head>
<body>

  <section class="card card-front">
    <div class="emblem-placeholder" role="img" aria-label="Emblem: telephone with a medical cross"></div>
    <h1 class="doctor-name">Dr. Lumi Harcourt</h1>
    <p class="doctor-credentials">M.B.B.S., F.C.G.F.C.</p>
    <p class="doctor-role">Family General Practitioner</p>
  </section>

  <section class="card card-back">
    <div class="hours-panel">
      <h2 class="hours-title">Working Hours</h2>
      <table class="hours-table">
        <tr><td class="day">Monday</td><td class="time">7 am - 7 pm</td></tr>
        <tr><td class="day">Tuesday</td><td class="time">7 am - 12 pm</td></tr>
        <tr><td class="day">Wednesday</td><td class="time">7 am - 10 pm</td></tr>
        <tr><td class="day">Thursday</td><td class="time">7 am - 12 pm</td></tr>
        <tr><td class="day">Friday</td><td class="time">7 am - 8 pm</td></tr>
        <tr><td class="day">Saturday</td><td class="time">8 am - 10 pm</td></tr>
        <tr><td class="day">Sunday</td><td class="time">CLOSED</td></tr>
      </table>
    </div>
    <address class="contact-block">
      <div class="contact-row">
        <span class="contact-label">A:</span>
        <span>Upper Level Harbour Court,<br>Wrenfield Plaza Shopping Centre,<br>Wrenfield Hill, NSW 2199</span>
      </div>
      <div class="contact-gap"></div>
      <div class="contact-row"><span class="contact-label">P:</span><span>02 5550 1400</span></div>
      <div class="contact-row"><span class="contact-label">F:</span><span>02 5550 1233</span></div>
    </address>
  </section>

</body>
</html>
```